Business card design for new, innovative company - BluePlinth

We are a new company looking for a business card design that is fun, different and quirky. Must use corporate colour green - CMYK C:55, M:0, Y:100, K:0, and corporate colour grey - C:0, M:0, Y: 0, K:70.

We have developed the first real time data application, in which people are able to profile the data of their existing customers in order to pull out more good fit clients to direct their marketing activities at.

Industry/Entity Type

Marketing

Requirements
Must have
• Logo, name, title, telephone number, fax number, email, website, address

```html
<!DOCTYPE html>
<html lang="en">
<head>
<meta charset="utf-8">
<title>BluePlinth business card</title>
<link rel="stylesheet" href="https://fonts.googleapis.com/css2?family=Arimo:wght@400;700&display=swap">
<style>
  :root {
    --brand-green: #7ac143;
    --brand-grey: #6d6e71;
    --card-dark: #58595b;
    --card-darker: #4a4b4d;
    --paper: #ffffff;
    --paper-shade: #e9eaeb;
    --text-light: #f2f2f2;
    --logo-faint: #d6d7d8;
    --stage: #e4e4e2;
  }
  * { margin: 0; padding: 0; box-sizing: border-box; }
  html, body {
    width: 1200px; height: 871px; overflow: hidden;
    background: var(--stage);
    font-family: "Arimo", Arial, sans-serif;
  }
  .stage {
    width: 1200px; height: 871px;
    display: flex; align-items: center; justify-content: center; gap: 48px;
  }
  .card {
    position: relative;
    width: 520px; height: 336px;
    overflow: hidden;
    box-shadow: 0 10px 28px rgba(0,0,0,0.25);
  }

  /* Back side */
  .card-back {
    background: linear-gradient(160deg, var(--brand-grey) 0%, var(--card-dark) 55%, var(--card-darker) 100%);
  }
  .card-back .wordmark {
    position: absolute; right: 34px; bottom: 96px;
    font-size: 44px; font-weight: 700; letter-spacing: -1.5px;
    color: var(--logo-faint);
  }

  /* Front side */
  .card-front { background: var(--card-dark); }
  .front-header {
    position: absolute; left: 0; top: 0; width: 100%; height: 140px;
    background: linear-gradient(100deg, var(--paper) 55%, var(--paper-shade) 100%);
  }
  .front-header .wordmark {
    position: absolute; left: 150px; top: 42px;
    font-size: 54px; font-weight: 700; letter-spacing: -2px;
    color: var(--brand-green);
  }
  .divider {
    position: absolute; left: 0; top: 140px; width: 100%; height: 4px;
    background: var(--brand-green);
  }
  .divider-tail { position: absolute; left: 78px; top: 143px; }
  .holder-name {
    position: absolute; left: 32px; top: 180px;
    font-size: 16px; color: var(--brand-green);
  }
  .contact {
    position: absolute; left: 196px; top: 168px;
    list-style: none; color: var(--text-light); font-size: 12.5px;
  }
  .contact li { display: flex; align-items: center; height: 23px; }
  .contact .icon { width: 26px; display: inline-flex; }
  .contact .address { padding-left: 0; }
  .contact .web { padding-left: 26px; }
</style>
</head>
<body>
<main class="stage">
  <section class="card card-back" aria-label="Card back">
    <span class="wordmark">BluePlinth</span>
  </section>

  <section class="card card-front" aria-label="Card front">
    <header class="front-header">
      <span class="wordmark">BluePlinth</span>
    </header>
    <div class="divider"></div>
    <svg class="divider-tail" width="22" height="12" viewBox="0 0 22 12" aria-hidden="true">
      <polygon points="1,0 21,0 11,11" fill="#ffffff" stroke="#7ac143" stroke-width="1.6"/>
    </svg>

    <p class="holder-name">Jenna Caldwell</p>

    <ul class="contact">
      <li class="address">22c Fenwick Road, Ely, Cambridgeshire, CB7 4QT</li>
      <li><span class="icon">
        <svg width="10" height="14" viewBox="0 0 10 14" aria-hidden="true"><rect x="1" y="1" width="8" height="12" rx="1.5" fill="none" stroke="#7ac143" stroke-width="1.4"/><circle cx="5" cy="10.5" r="0.9" fill="#7ac143"/></svg>
      </span>M: 07700 900418</li>
      <li><span class="icon">
        <svg width="14" height="12" viewBox="0 0 14 12" aria-hidden="true"><path d="M1 4 Q7 0 13 4 L11 6 L9 4.5 L5 4.5 L3 6 Z" fill="#7ac143"/><rect x="3" y="6.5" width="8" height="5" rx="1" fill="none" stroke="#7ac143" stroke-width="1.3"/></svg>
      </span>T: 01632 960735</li>
      <li><span class="icon">
        <svg width="14" height="10" viewBox="0 0 14 10" aria-hidden="true"><rect x="0.7" y="0.7" width="12.6" height="8.6" fill="none" stroke="#7ac143" stroke-width="1.3"/><polyline points="1,1 7,6 13,1" fill="none" stroke="#7ac143" stroke-width="1.3"/></svg>
      </span>E: jenna.caldwell@northledgetrade.com</li>
      <li><span class="icon">
        <svg width="13" height="13" viewBox="0 0 13 13" aria-hidden="true"><circle cx="6.5" cy="6.5" r="2.4" fill="none" stroke="#7ac143" stroke-width="1.4"/><path d="M8.9 6.5 V8 Q8.9 9.8 10.6 9.4 Q12 9 12 6.5 A5.5 5.5 0 1 0 9.3 11.2" fill="none" stroke="#7ac143" stroke-width="1.4"/></svg>
      </span></li>
      <li class="web">www.blueplinth.com</li>
    </ul>
  </section>
</main>
</body>
</html>
```